IV Nutritional Therapy Website Design

We are working with an IV Therapy company in California. They provide iv hydration services throughout California.

Some sites to use for inspiration:
https://www.kelvarowellness.com
https://quorvanest.com
https://talbrickcare.com (I love this option matrix. We need a nice way to present this on the homepage)
https://plimmerhaus.com

Thank you for taking the time to consider designing a website for us. We are web developers based in Stockton, CA, USA. Most of our projects go through the same process. Understanding this process may help you win a project with us. We custom-code all of our websites in-house. We don’t have any requirements as to what tools you use for your design, but we ask that you follow these guidelines.

IMAGES:
If you use any images or icons in the design, we ask that you have a link to the asset so we can purchase the image/icon. Most of the designs we submit do not have the customer’s images on them unless they have some great images. Be creative; show us the feeling you are trying to portray with your image choices. Use any royalty-free site you choose. We subscribe to Veltro and mainly use their images, but we can purchase images outside of Veltro. PLEASE NOTE: we will not submit designs to clients with watermarks on the images.

FONTS:
We ask that you identify the fonts you’re using in the design. This can be done in a message if you want. We typically use Google Fonts and Veltro Fonts.

CONTENT:
We're always open to different content and ideas. We often submit designs with stock images so the client can see our vision. We typically take pictures after the website launch to use their images with our vision. Lorem Ipsum is fine for paragraphs, but we ask that you make the Headers with correct English. We want to be able to show the vision and identify the sections of the website.

INSPIRATION:
We typically add a couple of links in the brief of websites we like to help you get started in your design.

REVISIONS:
We do not often ask for revisions of the designs unless we see something in the design that may not appeal to the client. If there are slight changes that we want to make, we do that in the development process.

FEEDBACK:
We rarely give feedback on designs during the design process. We are working on many website projects and do not have the time to provide feedback. We usually respond if your request is well thought out and asks specific questions, but a note asking “feedback, please” usually goes unanswered.

```html
<!DOCTYPE html>
<html lang="en">
<head>
<meta charset="utf-8">
<title>Verdalis Hydration — IV Nutritional Therapy</title>
<link href="https://fonts.googleapis.com/css2?family=Poppins:wght@400;500;600;700;800&display=swap" rel="stylesheet">
<style>
:root{
  --navy:#1e3a8f;
  --navy-deep:#0f2d6b;
  --green:#8fb04e;
  --green-light:#e8eee0;
  --orange:#f0a31c;
  --gold:#e0a515;
  --white:#ffffff;
  --ink:#222;
  --footer:#111111;
}
*{margin:0;padding:0;box-sizing:border-box}
html,body{width:1200px;height:3608px;overflow:hidden}
body{font-family:'Poppins',sans-serif;color:var(--ink);background:var(--white);position:relative}
section,header,footer{position:absolute;left:0;width:1200px}

/* header */
.site-header{top:0;height:86px;background:var(--white)}
.brand{position:absolute;left:115px;top:28px;width:240px;font-weight:700;font-size:17px;line-height:26px;color:var(--navy);display:flex;align-items:center;gap:8px;white-space:nowrap}
.brand-dot{width:12px;height:12px;background:var(--green);border-radius:50%;flex:none}
.main-nav{position:absolute;left:375px;top:28px;display:flex;gap:36px}
.main-nav a{font-weight:600;font-size:18px;line-height:26px;color:var(--ink);text-decoration:none;white-space:nowrap}

/* hero */
.hero{top:86px;height:512px;background:linear-gradient(180deg,#dfeaf3 0%,#cfe0ee 45%,#bcd5e8 100%)}
.hero-bag{position:absolute;left:95px;top:80px;width:240px;height:432px;background:linear-gradient(160deg,#e9eef2,#c7d3dc 50%,#9fb2a0);border-radius:24px 24px 8px 8px}
.hero-title{position:absolute;left:441px;top:98px;width:740px;font-weight:800;font-size:60px;line-height:60px;color:var(--navy);letter-spacing:-0.5px;white-space:nowrap}
.btn{display:inline-flex;align-items:center;justify-content:center;font-weight:700;text-decoration:none;text-transform:uppercase;white-space:nowrap}
.btn-green{background:var(--green);color:var(--navy);border-right:8px solid var(--navy)}
.hero .btn{position:absolute;left:442px;top:284px;width:181px;height:56px;font-size:17px}

/* about */
.about{top:598px;height:631px;background:var(--navy);overflow:hidden}
.about-photo{position:absolute;left:0;top:0;width:1200px;height:631px;background:linear-gradient(120deg,#e8ecef,#f3f3f4 50%,#d9dde0);clip-path:polygon(832px 0,1200px 0,1200px 631px,585px 631px)}
.about h2{position:absolute;left:113px;top:112px;font-weight:700;font-size:37px;color:var(--green)}
.about p{position:absolute;left:113px;top:200px;width:535px;font-size:16.4px;line-height:28.3px;color:var(--white);text-align:justify;hyphens:auto}
.about .btn{position:absolute;left:112px;top:463px;width:179px;height:56px;font-size:17px;background:var(--green);color:var(--navy);border-right:8px solid var(--white)}

/* pricing */
.pricing{top:1229px;height:788px;background:linear-gradient(180deg,#ffffff 0%,#f4f4f6 40%,#e4e5e9 100%)}
.section-title{position:absolute;left:0;width:100%;text-align:center;font-weight:800;font-size:42px;color:var(--navy-deep)}
.pricing .section-title{top:103px}
.plan{position:absolute;top:210px;width:311px;height:422px;background:var(--white);text-align:center}
.plan-top{height:174px;background:var(--green-light);padding-top:32px}
.plan-kicker{font-size:14px;color:#444}
.plan-name{margin-top:18px;font-weight:700;font-size:21px;color:var(--navy-deep);white-space:nowrap}
.plan-price{margin-top:4px;display:flex;justify-content:center;align-items:baseline;gap:8px}
.plan-price .cur{font-weight:700;font-size:15px;color:var(--navy-deep)}
.plan-price .amt{font-weight:700;font-size:36px;color:var(--orange);line-height:44px}
.plan-price .labs{font-size:12px;color:var(--navy-deep)}
.plan-note{margin-top:30px;font-size:12.5px;color:#444}
.plan .btn-green{margin-top:26px;width:181px;height:56px;font-size:17px}
.btn-navy{background:var(--navy-deep);color:var(--white);width:122px;height:44px;font-size:17px;margin-top:22px}
.plan-featured{box-shadow:0 8px 20px rgba(0,0,0,.1)}
.plan-featured .badge{position:absolute;top:-20px;left:0;width:100%;height:20px;background:var(--gold);color:var(--white);font-size:12px;font-weight:600;line-height:20px}
.plan-featured .plan-top{background:var(--navy-deep)}
.plan-featured .plan-kicker,.plan-featured .plan-name,.plan-featured .cur,.plan-featured .labs{color:var(--white)}

/* what to bring */
.bring{top:2017px;height:451px;background:radial-gradient(ellipse at 60% 40%,#a9c972,#93b857 60%,#86ad4c)}
.bring .section-title{top:68px;font-weight:700;font-size:45px}
.bring-intro{position:absolute;left:240px;top:150px;width:720px;text-align:center;font-size:16px;line-height:24px;color:var(--white)}
.benefit{position:absolute;top:240px;width:180px;text-align:center}
.benefit-ring{width:86px;height:86px;margin:0 auto;border:2px dashed var(--white);border-radius:50%;display:flex;align-items:center;justify-content:center}
.benefit-label{margin-top:14px;font-weight:600;font-size:17px;color:var(--navy);white-space:nowrap}

/* plan overview */
.overview{top:2468px;height:718px;background:linear-gradient(135deg,#f6f6f7 0%,#e8e8ea 35%,#f5f5f6 55%,#e6e6e8 80%,#f2f2f3 100%)}
.overview .section-title{top:127px;left:-6px}
.matrix{position:absolute;left:266px;top:185px;width:658px;height:433px;background:var(--white);box-shadow:0 2px 8px rgba(0,0,0,.15);display:flex;gap:10px;padding:21px 20px 20px}
.col{display:flex;flex-direction:column}
.col-labels{width:219px}
.col-plan{width:123px}
.cell{height:37px;display:flex;align-items:center;justify-content:center;font-size:13px;color:var(--white);white-space:nowrap}
.cell.head{height:42px;font-size:12px;padding-top:6px}
.cell.foot{flex:1}
.col-labels .cell{justify-content:flex-start;padding-left:36px;font-size:14px}
.col-labels .cell:nth-child(odd){background:#2d2d2d}
.col-labels .cell:nth-child(even){background:#474747}
.col-labels .head{background:#555 !important;border-top:4px solid #2d2d2d}
.col-blue .cell:nth-child(odd){background:#1f3e96}
.col-blue .cell:nth-child(even){background:#2d4ca6}
.col-blue .head{border-top:4px solid #14306e}
.col-green .cell:nth-child(odd){background:#8cb251}
.col-green .cell:nth-child(even){background:#a0c26c}
.col-green .head{border-top:4px solid #7ea047}
.col-grey .cell:nth-child(odd){background:#6f6f6f}
.col-grey .cell:nth-child(even){background:#828282}
.col-grey .head{border-top:4px solid #5e5e5e}
.cell .tag{font-size:12px}

/* footer */
.site-footer{top:3186px;height:422px;background:var(--footer);color:var(--white)}
.footer-brand{position:absolute;left:0;width:100%;top:110px;text-align:center;font-weight:700;font-size:36px;color:var(--navy)}
.footer-brand .brand-dot{display:inline-block;vertical-align:middle;margin-right:12px}
.footer-nav{position:absolute;top:223px;left:0;width:100%;display:flex;justify-content:center;gap:36px}
.footer-nav a{color:var(--white);font-weight:600;font-size:18px;text-decoration:none;white-space:nowrap}
.social{position:absolute;top:289px;left:0;width:100%;display:flex;justify-content:center;gap:30px}
.social span{width:16px;height:16px;border-radius:50%;background:var(--white)}
.footer-rule{position:absolute;top:356px;left:112px;width:973px;height:1px;background:#555}
.copyright{position:absolute;top:373px;left:115px;font-size:16px}
</style>
</head>
<body>

<header class="site-header">
  <div class="brand"><span>VERDALIS HYDRATION</span><span class="brand-dot"></span></div>
  <nav class="main-nav">
    <a href="#">Appearance</a><a href="#">IV Nutritional Therapy</a><a href="#">Treatments</a><a href="#">Conditions</a><a href="#">About Us</a>
  </nav>
</header>

<section class="hero" role="img" aria-label="Rippling water surface in soft blue light">
  <div class="hero-bag" role="img" aria-label="IV bag filled with sliced fruit"></div>
  <h1 class="hero-title">WELCOME TO<br>VERDALIS HYDRATION</h1>
  <a class="btn btn-green" href="#">Get Started</a>
</section>

<section class="about">
  <div class="about-photo" role="img" aria-label="Gloved hand holding an IV bag filled with fruit"></div>
  <h2>ABOUT US</h2>
  <p>Sed ut perspiciatis unde omnis iste natus error sit voluptatem accusantium doloremque laudantium, totam rem aperiam, eaque ipsa quae ab illo inventore veritatis et quasi architecto beatae vitae dicta sunt explicabo. Nemo enim ipsam voluptatem quia voluptas sit aspernatur aut odit aut fugit, sed quia consequuntur magni dolores eos qui ratione voluptatem sequi nesciunt. Neque porro quisquam est, qui dolorem ipsum quia dolor sit amet, consectetur, adipisci velit.</p>
  <a class="btn" href="#">Read More</a>
</section>

<section class="pricing">
  <h2 class="section-title">PRICING</h2>
  <div class="plan" style="left:112px">
    <div class="plan-top">
      <div class="plan-kicker">Lorem Ipsum is simply</div>
      <div class="plan-name">HORMONE FOCUS</div>
      <div class="plan-price"><span class="cur">$</span><span class="amt">365</span><span class="labs">PLUS LABS</span></div>
    </div>
    <div class="plan-note">Lorem Ipsum is simply dummy</div>
    <a class="btn btn-green" href="#">Get Started</a><br>
    <a class="btn btn-navy" href="#">More Info</a>
  </div>
  <div class="plan plan-featured" style="left:444px">
    <div class="badge">MOST POPULAR</div>
    <div class="plan-top">
      <div class="plan-kicker">Lorem Ipsum is simply</div>
      <div class="plan-name">OVERALL HEALTH</div>
      <div class="plan-price"><span class="cur">$</span><span class="amt">900</span><span class="labs">PLUS LABS</span></div>
    </div>
    <div class="plan-note">Lorem Ipsum is simply dummy</div>
    <a class="btn btn-green" href="#">Get Started</a><br>
    <a class="btn btn-navy" href="#">More Info</a>
  </div>
  <div class="plan" style="left:777px">
    <div class="plan-top">
      <div class="plan-kicker">Lorem Ipsum is simply</div>
      <div class="plan-name">COMPREHENSIVE HEALTH</div>
      <div class="plan-price"><span class="cur">$</span><span class="amt">2,135</span><span class="labs">PLUS LABS</span></div>
    </div>
    <div class="plan-note">Lorem Ipsum is simply dummy</div>
    <a class="btn btn-green" href="#">Get Started</a><br>
    <a class="btn btn-navy" href="#">More Info</a>
  </div>
</section>

<section class="bring" role="img" aria-label="Soft-focus fruit and IV bag tinted green">
  <h2 class="section-title">What To Bring</h2>
  <p class="bring-intro">Lorem Ipsum is simply dummy text of the printing and typesetting industry. Lorem Ipsum has been the industry's standard dummy text ever since the 1500s</p>
  <div class="benefit" style="left:324px">
    <div class="benefit-ring"><svg width="40" height="44" viewBox="0 0 40 44" fill="none" stroke="#fff" stroke-width="2"><path d="M20 3 L35 9 V21 C35 31 28 38 20 41 C12 38 5 31 5 21 V9 Z"/><circle cx="20" cy="22" r="8"/><path d="M20 18v8M16 22h8"/></svg></div>
    <div class="benefit-label">Immune Health</div>
  </div>
  <div class="benefit" style="left:510px">
    <div class="benefit-ring"><svg width="46" height="44" viewBox="0 0 46 44" fill="none" stroke="#fff" stroke-width="2"><path d="M23 6l8 5v9l-8 5-8-5v-9z"/><path d="M31 20l8 5v9M15 20l-8 5v9M23 25v9"/><circle cx="7" cy="36" r="2"/><circle cx="39" cy="36" r="2"/></svg></div>
    <div class="benefit-label">Restore Hormones</div>
  </div>
  <div class="benefit" style="left:704px">
    <div class="benefit-ring"><svg width="40" height="44" viewBox="0 0 40 44" fill="none" stroke="#fff" stroke-width="2"><path d="M12 40v-8c-5-3-8-8-8-14C4 10 11 4 20 4s16 6 16 14l3 8h-4v6c0 2-2 4-4 4h-5v4"/><circle cx="20" cy="18" r="8"/><path d="M21 12l-4 7h5l-3 6"/></svg></div>
    <div class="benefit-label">Boost Energy</div>
  </div>
</section>

<section class="overview">
  <h2 class="section-title">PLAN OVERVIEW</h2>
  <div class="matrix">
    <div class="col col-labels">
      <div class="cell head"></div>
      <div class="cell">Lorem Ipsum is simply</div><div class="cell">Lorem Ipsum is simply</div><div class="cell">Lorem Ipsum is simply</div><div class="cell">Lorem Ipsum is simply</div>
      <div class="cell">Lorem Ipsum is simply</div><div class="cell">Lorem Ipsum is simply</div><div class="cell">Lorem Ipsum is simply</div><div class="cell">Lorem Ipsum is simply</div>
      <div class="cell foot"></div>
    </div>
    <div class="col col-plan col-blue">
      <div class="cell head">HOMEONE FOCUS</div>
      <div class="cell"><svg width="16" height="14"><path d="M2 7l4 4 8-9" stroke="#fff" stroke-width="2.5" fill="none"/></svg></div>
      <div class="cell"><svg width="16" height="14"><path d="M2 7l4 4 8-9" stroke="#fff" stroke-width="2.5" fill="none"/></svg></div>
      <div class="cell"><svg width="16" height="14"><path d="M2 7l4 4 8-9" stroke="#fff" stroke-width="2.5" fill="none"/></svg></div>
      <div class="cell"><svg width="14" height="14"><path d="M2 2l10 10M12 2L2 12" stroke="#fff" stroke-width="3"/></svg></div>
      <div class="cell"><svg width="14" height="14"><path d="M2 2l10 10M12 2L2 12" stroke="#fff" stroke-width="3"/></svg></div>
      <div class="cell"><svg width="14" height="14"><path d="M2 2l10 10M12 2L2 12" stroke="#fff" stroke-width="3"/></svg></div>
      <div class="cell"><svg width="14" height="14"><path d="M2 2l10 10M12 2L2 12" stroke="#fff" stroke-width="3"/></svg></div>
      <div class="cell"><svg width="14" height="14"><path d="M2 2l10 10M12 2L2 12" stroke="#fff" stroke-width="3"/></svg></div>
      <div class="cell foot"></div>
    </div>
    <div class="col col-plan col-green">
      <div class="cell head">HOMEONE FOCUS</div>
      <div class="cell"><svg width="16" height="14"><path d="M2 7l4 4 8-9" stroke="#fff" stroke-width="2.5" fill="none"/></svg></div>
      <div class="cell"><svg width="16" height="14"><path d="M2 7l4 4 8-9" stroke="#fff" stroke-width="2.5" fill="none"/></svg></div>
      <div class="cell"><svg width="16" height="14"><path d="M2 7l4 4 8-9" stroke="#fff" stroke-width="2.5" fill="none"/></svg></div>
      <div class="cell"><span class="tag">FULL</span></div>
      <div class="cell"><span class="tag">FULL</span></div>
      <div class="cell"><span class="tag">FULL</span></div>
      <div class="cell"><svg width="16" height="14"><path d="M2 7l4 4 8-9" stroke="#fff" stroke-width="2.5" fill="none"/></svg></div>
      <div class="cell"><svg width="16" height="14"><path d="M2 7l4 4 8-9" stroke="#fff" stroke-width="2.5" fill="none"/></svg></div>
      <div class="cell foot"></div>
    </div>
    <div class="col col-plan col-grey">
      <div class="cell head">HOMEONE FOCUS</div>
      <div class="cell"><svg width="16" height="14"><path d="M2 7l4 4 8-9" stroke="#fff" stroke-width="2.5" fill="none"/></svg></div>
      <div class="cell"><svg width="16" height="14"><path d="M2 7l4 4 8-9" stroke="#fff" stroke-width="2.5" fill="none"/></svg></div>
      <div class="cell"><svg width="16" height="14"><path d="M2 7l4 4 8-9" stroke="#fff" stroke-width="2.5" fill="none"/></svg></div>
      <div class="cell"><span class="tag">COMPREHENSIVE</span></div>
      <div class="cell"><span class="tag">COMPREHENSIVE</span></div>
      <div class="cell"><span class="tag">COMPREHENSIVE</span></div>
      <div class="cell"><svg width="16" height="14"><path d="M2 7l4 4 8-9" stroke="#fff" stroke-width="2.5" fill="none"/></svg></div>
      <div class="cell"><svg width="16" height="14"><path d="M2 7l4 4 8-9" stroke="#fff" stroke-width="2.5" fill="none"/></svg></div>
      <div class="cell foot"></div>
    </div>
  </div>
</section>

<footer class="site-footer">
  <div class="footer-brand"><span class="brand-dot"></span>VERDALIS HYDRATION</div>
  <nav class="footer-nav">
    <a href="#">Appearance</a><a href="#">IV Nutritional Therapy</a><a href="#">Treatments</a><a href="#">Conditions</a><a href="#">About Us</a>
  </nav>
  <div class="social" aria-label="Social links"><span></span><span></span><span></span><span></span><span></span></div>
  <div class="footer-rule"></div>
  <div class="copyright">© 2023&nbsp; Verdalis Hydration</div>
</footer>

</body>
</html>
```